Looking for a creative label design for our retail coffee bags

We are a coffee manufacturer (coffee roaster) looking to re-brand our retail label for our coffee bags. Our main coffee blend that we sell is our Harborline Velvet Blend. You can use this name when creating the label. We are going for a look that represents our company as a coffee roaster. Please reference our website (www.brindlemugworks.com) and our Facebook page to learn more about our company and to give you more inspiration on creating this design.

Target Market(s)

Retail customers/grocery stores

Industry/Entity Type

Manufacturer

Requirements
Must have
• The size of the label has to be 3" width x 4" height

Logo must be Black
Nice to have
• We currently incorporate a color on our labels for each blend. For example, Harborline Velvet Blend (royal blue), Decaffeinated Blend (red), Breakfast Blend (green), Flavored coffees (gold).

Rustic/vintage style

```html
<!DOCTYPE html>
<html lang="en">
<head>
<meta charset="utf-8">
<title>Brindle Mugworks – Retail Coffee Labels</title>
<link rel="stylesheet" href="https://fonts.googleapis.com/css2?family=Oswald:wght@600&family=Kaushan+Script&display=swap">
<style>
  :root {
    --page: #ffffff;
    --band: #d4d5d7;
    --band-light: #e6e7e8;
    --script: #f4f4f4;
    --logo: #1d1b1c;
    --logo-text: #ffffff;
    --blue-a: #1f55a8;
    --blue-b: #13254f;
    --blue-ink: #25376f;
    --gold-a: #e1c46a;
    --gold-b: #8c6c2a;
    --gold-ink: #b8953f;
    --green-a: #2e8a4e;
    --green-b: #0f4a2c;
    --green-ink: #1f6b3b;
    --red-a: #b8262a;
    --red-b: #3e0d0f;
    --red-ink: #97252a;
  }
  * { box-sizing: border-box; margin: 0; padding: 0; }
  html, body { width: 900px; height: 1200px; overflow: hidden; background: var(--page); }
  .sheet { position: relative; width: 900px; height: 1200px; }

  .label { position: absolute; width: 269px; height: 360px; }
  .label--blue  { left: 120px; top: 157px; }
  .label--gold  { left: 520px; top: 157px; }
  .label--green { left: 120px; top: 711px; }
  .label--red   { left: 520px; top: 711px; }

  .label__art {
    position: absolute; left: 0; top: 0; width: 100%; height: 259px;
  }
  .label--blue  .label__art { background: linear-gradient(100deg, var(--blue-a), var(--blue-b)); }
  .label--gold  .label__art { background: linear-gradient(100deg, var(--gold-a), var(--gold-b)); }
  .label--green .label__art { background: linear-gradient(100deg, var(--green-a), var(--green-b)); }
  .label--red   .label__art { background: linear-gradient(100deg, var(--red-a), var(--red-b)); }

  .brand {
    position: absolute; left: 79px; top: 75px; width: 110px; height: 110px;
    border-radius: 50%; background: var(--logo);
    display: flex; flex-direction: column; align-items: center; justify-content: center;
    font-family: "Oswald", sans-serif; font-weight: 600; color: var(--logo-text);
    text-transform: uppercase; line-height: 1.05; letter-spacing: 0.5px;
  }
  .brand__line { font-size: 17px; }

  .label__band {
    position: absolute; left: 0; top: 259px; width: 100%; height: 101px;
    background: linear-gradient(180deg, var(--band-light), var(--band) 40%, var(--band));
    text-align: center;
  }
  .band__script {
    display: block; padding: 18px 0 0 48px;
    font-family: "Kaushan Script", cursive; font-size: 19px; color: var(--script);
    line-height: 1;
  }
  .band__title {
    display: block; margin-top: 6px;
    font-family: "Oswald", sans-serif; font-weight: 600; font-size: 25px;
    text-transform: uppercase; line-height: 1.1; letter-spacing: 0.2px;
  }
  .label--blue  .band__title { color: var(--blue-ink); }
  .label--gold  .band__title { color: var(--gold-ink); }
  .label--green .band__title { color: var(--green-ink); }
  .label--red   .band__title { color: var(--red-ink); }
</style>
</head>
<body>
<main class="sheet">

  <section class="label label--blue">
    <div class="label__art" role="img" aria-label="Royal blue panel with large outlined coffee bean pattern"></div>
    <div class="brand"><span class="brand__line">Brindle</span><span class="brand__line">Mugworks</span></div>
    <div class="label__band">
      <span class="band__script">Freshly Roasted</span>
      <span class="band__title">Harborline Velvet</span>
    </div>
  </section>

  <section class="label label--gold">
    <div class="label__art" role="img" aria-label="Gold panel with large outlined coffee bean pattern"></div>
    <div class="brand"><span class="brand__line">Brindle</span><span class="brand__line">Mugworks</span></div>
    <div class="label__band">
      <span class="band__script">Freshly Roasted</span>
      <span class="band__title">Flavored Coffees</span>
    </div>
  </section>

  <section class="label label--green">
    <div class="label__art" role="img" aria-label="Green panel with large outlined coffee bean pattern"></div>
    <div class="brand"><span class="brand__line">Brindle</span><span class="brand__line">Mugworks</span></div>
    <div class="label__band">
      <span class="band__script">Freshly Roasted</span>
      <span class="band__title">Breakfast Blend</span>
    </div>
  </section>

  <section class="label label--red">
    <div class="label__art" role="img" aria-label="Red panel with large outlined coffee bean pattern"></div>
    <div class="brand"><span class="brand__line">Brindle</span><span class="brand__line">Mugworks</span></div>
    <div class="label__band">
      <span class="band__script">Freshly Roasted</span>
      <span class="band__title">Decaffeinated Blend</span>
    </div>
  </section>

</main>
</body>
</html>
```